Web-Design for Electrcian Company

Our Customer is a small business electrian in Switzerland. He is looking for a fresh and innovative website design. He is well known for his extra service, and that they always go for the extra-mile! In his logo you also see that positive and fresh image the try to bring to the customer. the main colors are black, red and white.

the website structure will be:

- home
- services (with submenu for each service)
- references (with submenu for each category of services)
- about us (2 submenus: history and staff)
- links
- Contact

Reason: We are discussing the Proposals with the customer right now

Target Market(s)

Architects, building owners, people from the age of 35 up...

Industry/Entity Type

Small Business

```html
<!DOCTYPE html>
<html lang="en">
<head>
<meta charset="utf-8">
<title>Funkenhof Haustechnik</title>
<link href="https://fonts.googleapis.com/css2?family=Oswald:wght@500;600&family=Fira+Sans:wght@400;600&family=Arimo:wght@400&display=swap" rel="stylesheet">
<style>
:root{
  --red:#db1424;
  --red-1:#f43737;
  --red-2:#e91c2c;
  --red-3:#d9141e;
  --red-4:#a30f1a;
  --red-top:#b80f1c;
  --ink:#1c1c1c;
  --grey:#7a7a7a;
  --line:#e2e2e2;
  --footer:#2e2e2e;
  --footer-line:#3a3a3a;
  --footer-text:#6a6a6a;
  --white:#fff;
}
*{margin:0;padding:0;box-sizing:border-box}
html,body{width:758px;height:1200px;overflow:hidden;background:var(--white)}
body{position:relative;font-family:"Arimo",Arial,sans-serif;color:var(--grey)}
.cond{font-family:"Oswald","Arial Narrow",sans-serif;text-transform:uppercase}

.site-header{position:absolute;top:0;left:0;width:758px;height:102px;border-bottom:1px solid var(--line)}
.brand{position:absolute;left:0;width:758px;top:42px;display:flex;align-items:center;justify-content:center;gap:10px}
.brand-name{font-family:"Fira Sans",Arial,sans-serif;font-weight:600;font-size:17px;color:var(--ink);letter-spacing:.2px}
.brand-mark{width:12px;height:12px;background:var(--red)}

.main-nav{position:absolute;top:102px;left:0;width:758px;height:62px;border-bottom:1px solid var(--line)}
.main-nav ul{list-style:none;position:absolute;left:115px;width:529px;height:62px;display:flex;border-right:1px solid var(--line)}
.main-nav li{width:88.2px;height:62px;border-left:1px solid var(--line);display:flex;align-items:center;justify-content:center;font-size:10.5px;font-weight:500;color:var(--ink)}
.main-nav li.active{background:var(--red);color:var(--white);border-color:var(--red)}
.main-nav li.active + li.active{border-left-color:#b80f1c}
.submenu{position:absolute;left:205px;top:173px;width:88px;height:77px;background:#262626;color:var(--white);font-size:9px;line-height:10px;font-weight:500;display:flex;flex-direction:column;justify-content:center;align-items:center;z-index:2}

.hero{position:absolute;left:115px;top:164px;width:529px;height:288px;background:linear-gradient(100deg,#c9ccd0 0%,#8e949b 30%,#b6aa98 55%,#d8d2c8 80%,#c4bfb6 100%)}
.hero-rule{position:absolute;top:452px;left:0;width:758px;border-top:1px solid var(--line)}
.dots{position:absolute;top:467px;left:356px;display:flex;gap:14px}
.dots span{width:6px;height:6px;border-radius:50%;background:#e6e6e6}
.dots span.on{background:var(--ink)}

.features{position:absolute;left:115px;top:489px;width:529px;height:223px;display:flex}
.feature{width:132.25px;height:223px;padding:23px 18px 0 10px;color:var(--white);border-top:6px solid var(--red-top)}
.feature:nth-child(1){background:var(--red-1)}
.feature:nth-child(2){background:var(--red-2)}
.feature:nth-child(3){background:var(--red-3)}
.feature:nth-child(4){background:var(--red-4);border-top-color:var(--red-1)}
.feature h2{font-size:20px;font-weight:500;line-height:24px;margin-bottom:10px}
.feature p{font-size:8.2px;line-height:12.4px}
.feature a,.more{display:inline-block;font-size:6px;text-decoration:underline;margin-top:16px;text-transform:uppercase}
.feature a{color:var(--white)}

.block{position:absolute;top:745px}
.block h3{font-size:12.5px;font-weight:500;color:var(--ink);margin-bottom:16px}
.more{color:var(--red);position:absolute;top:194px;left:0;margin:0}
.intro{left:115px;width:240px}
.intro-photo{width:219px;height:83px;background:linear-gradient(180deg,#a9c1dc 0%,#dfe8f2 55%,#6a6d70 100%)}
.intro p{font-size:7px;line-height:10px;margin-top:20px}
.news{left:385px;width:124px}
.news-item{border-bottom:1px solid var(--line);padding-bottom:5px;margin-bottom:6px}
.news-item:last-of-type{border:none}
.news-item b{display:block;color:var(--red);font-weight:400;font-size:7px;text-transform:uppercase;line-height:9px;margin-bottom:1px}
.news-item p{font-size:6.8px;line-height:10.2px}
.todo{left:520px;width:130px}
.todo ul{list-style:none}
.todo li{display:flex;align-items:center;gap:7px;font-size:7px;height:14.6px}
.todo svg{width:10px;height:10px;flex:none}

.site-footer{position:absolute;top:980px;left:0;width:758px;height:220px;background:var(--footer)}
.fcol{position:absolute;top:36px;width:112px}
.fcol.wide{width:130px}
.fcol h4{font-size:12.5px;font-weight:500;color:var(--white);margin-bottom:22px}
.fcol ul{list-style:none}
.fcol li{font-size:5.6px;text-transform:uppercase;color:var(--footer-text);height:17px;line-height:16px;border-bottom:1px solid var(--footer-line)}
.fcol li::before{content:"•";margin-right:4px}
.fcol p{font-size:5.6px;line-height:10px;text-transform:uppercase;color:var(--footer-text)}
</style>
</head>
<body>
<header class="site-header">
  <div class="brand">
    <span class="brand-name">Funkenhof Haustechnik</span>
    <span class="brand-mark"></span>
  </div>
</header>

<nav class="main-nav cond">
  <ul>
    <li class="active">Home</li>
    <li class="active">Services</li>
    <li>References</li>
    <li>About us</li>
    <li>Links</li>
    <li>Contact</li>
  </ul>
</nav>
<div class="submenu cond"><span>Service1</span><span>Service2</span><span>Service3</span><span>Technologies</span></div>

<div class="hero" role="img" aria-label="Electrician in a yellow hard hat wiring an outdoor air conditioning unit"></div>
<div class="hero-rule"></div>
<div class="dots"><span class="on"></span><span></span><span></span></div>

<section class="features">
  <article class="feature"><h2 class="cond">Lorem</h2><p>In pede mi aliquet sit amemod intous tinci metus aesent justolobor tis qui lovinar actibulm sed anonec sagittis euisoerspi unde oistatu oluptcusm dolemque laudantiam rem aper iaipsqua ilnventore veritatis etquasi arh.</p><a>Read more</a></article>
  <article class="feature"><h2 class="cond">Ipsum</h2><p>Aesent justolobor tis qui lovinar actibulm sed anonec sagittis euisoerspi unde oistatu oluptcusue laudan tiam rem aper iaipsquaea. b ilnventore veritatis etquasi arhite eatae vitae dicta sunt explicbomo enim ipsa.</p><a>Read more</a></article>
  <article class="feature"><h2 class="cond">Dolor</h2><p>Ememod intous tinci metus aesent justolobor tis qui lovinar actibulm sed anonec sagittis euisoerspi unde oistatu oluptcusm dolemque laudantiam rem aper iaipsqilnven.</p><a>Read more</a></article>
  <article class="feature"><h2 class="cond">Sit amet</h2><p>In pede mi aliquet sit amemod intous tinci metus aesent justolobor tis qui lovinar actibulm sed anonec sagittis euisoerspi unde oistatu oluptcusm dolemque laudantiam rem aper iaipsquae ilnventore veritatis etquasi arhit.</p><a>Read more</a></article>
</section>

<section class="block intro">
  <h3 class="cond">Lorem ipsum dolor sit amet</h3>
  <div class="intro-photo" role="img" aria-label="Two business people in suits standing against a cloudy sky"></div>
  <p>In pede mi aliquet sit amemod intous tinci metus aesent justolobor tis qui lovinar actibulm sed anonec sagittis euisoerspi unde oistatu oluptcusm dolemque laudantiam rem aper iaipsquaea ilnventore veritatis etquasi arhite eatae vitae dicta sunt explicbomo enim ipsa.</p>
  <a class="more">Read more</a>
</section>

<section class="block news">
  <h3 class="cond">What s new?</h3>
  <div class="news-item"><b>Fri, Nov 18</b><p>In pede mi aliquet sit amemod intous tinci metus aesent justolobor tis qui lovinar actii unde.</p></div>
  <div class="news-item"><b>Wed, Nov 05</b><p>Eluptcusm dolemque laudantiam rem aper iaipsquaeab ilnventeritatis etquasi arhite eatae vit.</p></div>
  <div class="news-item"><b>Thu, Nov 07</b><p>Toluptas sit asperatur aut odit auted quia consequutu mages eos atione luptatem sequi nesciunu.</p></div>
  <a class="more">Read more</a>
</section>

<section class="block todo">
  <h3 class="cond">What we do?</h3>
  <ul>
    <li><svg viewBox="0 0 10 10"><circle cx="5" cy="5" r="5" fill="#db1424"/><path d="M2.8 5h4M5.3 3.3 7 5 5.3 6.7" stroke="#fff" stroke-width="1.1" fill="none"/></svg>Pede mi aliquet sit amem</li>
    <li><svg viewBox="0 0 10 10"><circle cx="5" cy="5" r="5" fill="#db1424"/><path d="M2.8 5h4M5.3 3.3 7 5 5.3 6.7" stroke="#fff" stroke-width="1.1" fill="none"/></svg>Intous tinci metus aesen</li>
    <li><svg viewBox="0 0 10 10"><circle cx="5" cy="5" r="5" fill="#db1424"/><path d="M2.8 5h4M5.3 3.3 7 5 5.3 6.7" stroke="#fff" stroke-width="1.1" fill="none"/></svg>Eluptcusm dolemque lauda</li>
    <li><svg viewBox="0 0 10 10"><circle cx="5" cy="5" r="5" fill="#db1424"/><path d="M2.8 5h4M5.3 3.3 7 5 5.3 6.7" stroke="#fff" stroke-width="1.1" fill="none"/></svg>Tiam rem aper iaipsquaea</li>
    <li><svg viewBox="0 0 10 10"><circle cx="5" cy="5" r="5" fill="#db1424"/><path d="M2.8 5h4M5.3 3.3 7 5 5.3 6.7" stroke="#fff" stroke-width="1.1" fill="none"/></svg>Anventeritatis etquasi arh</li>
    <li><svg viewBox="0 0 10 10"><circle cx="5" cy="5" r="5" fill="#db1424"/><path d="M2.8 5h4M5.3 3.3 7 5 5.3 6.7" stroke="#fff" stroke-width="1.1" fill="none"/></svg>Toluptas sit asperatur aut</li>
    <li><svg viewBox="0 0 10 10"><circle cx="5" cy="5" r="5" fill="#db1424"/><path d="M2.8 5h4M5.3 3.3 7 5 5.3 6.7" stroke="#fff" stroke-width="1.1" fill="none"/></svg>Odit auted quia consequutu</li>
    <li><svg viewBox="0 0 10 10"><circle cx="5" cy="5" r="5" fill="#db1424"/><path d="M2.8 5h4M5.3 3.3 7 5 5.3 6.7" stroke="#fff" stroke-width="1.1" fill="none"/></svg>Mages eos atione luptat</li>
    <li><svg viewBox="0 0 10 10"><circle cx="5" cy="5" r="5" fill="#db1424"/><path d="M2.8 5h4M5.3 3.3 7 5 5.3 6.7" stroke="#fff" stroke-width="1.1" fill="none"/></svg>Por quisqua estqui dolorem</li>
    <li><svg viewBox="0 0 10 10"><circle cx="5" cy="5" r="5" fill="#db1424"/><path d="M2.8 5h4M5.3 3.3 7 5 5.3 6.7" stroke="#fff" stroke-width="1.1" fill="none"/></svg>Consectetu adipisci elit sed</li>
  </ul>
  <a class="more">Read more</a>
</section>

<footer class="site-footer">
  <div class="fcol" style="left:115px"><h4 class="cond">About us</h4><ul><li>About us</li><li>Services</li><li>Work team</li><li>Awards</li><li>News</li></ul></div>
  <div class="fcol" style="left:250px"><h4 class="cond">Services</h4><ul><li>Researches</li><li>Planning</li><li>Development</li><li>Creative ideas</li><li>Impartial approach</li><li>Complex tasks</li><li>Outsourcing partnership</li><li>Support</li></ul></div>
  <div class="fcol" style="left:385px"><h4 class="cond">Follow us</h4><ul><li>Chirper</li><li>RSS</li><li>Circle Plus</li><li>Facelist</li></ul></div>
  <div class="fcol wide" style="left:520px"><h4 class="cond">Copyright</h4><p>Funkenhof Haustechnik © 2012 •<br>Privacy policy</p></div>
</footer>
</body>
</html>
```